HAIR EXTENSIONS

We need a web design for a company base in Chicago called Extensions by Corvella. We sale 100% human hair in Brazilian body wave deep wave straight or natural curl, Peruvian body wave straight or deep wave. Malaysian loose straight or body wave, in the chicago land.
We also ship hair to any city or country. We like to see design that use the colors pinks & grays, or would just like to see some design creative with colors thats inviting.

Also I'm using the quillmoss template, Home- banner contact us, about us, Features- product side/left sidebar, Shop- wish list /shopping cart/ tracking your order / checkout/ order received.
Porfolio-filterable 4column portfolio
Blog. Buy now

Industry/Entity Type

Hair

Number of Pages Required

4 page

Colors
aaaaaa
606060
dddddd
eea4c8
d3a5cc
b868aa
a6459a
ffc213
1b1b1b

Requirements
Must have
• I NEED THE DESIGNER TO DO THE 4 PAGE LIKE THIS.
• 1.HOME-PAGE BANNER CONTACT US SOME PRODUCT WITH SIDING IMAGES OF THE TOP PROUDCT
• 2.PRODUCT WITH SHOPPING CART- I WANT SIDING BARS FOR PRODUCT & SHOPPING CART WITH TRACKING YOUR ORDERS CHECK OUT & ORDER RECEIVED.
• 3.PORFOLIO PHOTO-I WANT A FEATURES FOR CUSTOMERS TO UPLOAN THERE PICTURE & BLOG ON THE PAGE
• 4.ABOUT US- TALK ABOUT ARE COMPAMY.
Nice to have
• hello designer
• I was working with a web developer for my site be for i came to pixelharborr & they build a site for me that i liked, You all can view it at www.Extensionsbycorvella.info
• long story short never could get them to finish the project after they got paid!!
• I know, why paid before its finish bad decision. So know I'm here starting over with you all.
• here is a list of my competition site
• www.lockshaventress.com
• www.velmatrade.com
• www.orlitasparlor.com
• So just to give some insight, I'm looking for something like the one i had builded.

```html
<!DOCTYPE html>
<html lang="en">
<head>
<meta charset="utf-8">
<title>Extensions by Corvella</title>
<link href="https://fonts.googleapis.com/css2?family=Open+Sans:wght@300;400;600;700;800&display=swap" rel="stylesheet">
<style>
:root{
  --pink:#d6196f;
  --pink-soft:#eea4c8;
  --ink:#1b1b1b;
  --dark:#2a2a2a;
  --grey:#606060;
  --grey-mid:#aaaaaa;
  --grey-light:#dddddd;
  --paper:#ffffff;
  --wash:#f3f3f3;
}
*{box-sizing:border-box;margin:0;padding:0}
html,body{width:918px;height:1200px;overflow:hidden;background:var(--paper);font-family:"Open Sans",Arial,sans-serif;color:var(--ink)}
.page{position:relative;width:918px;height:1200px}
.abs{position:absolute}

/* header */
.site-header{position:absolute;left:0;top:0;width:918px;height:105px;background:linear-gradient(#fff,#efefef)}
.brand{left:60px;top:24px;display:flex;align-items:center;gap:10px}
.brand-mark{width:14px;height:14px;background:var(--pink)}
.brand-name{font-size:28px;font-weight:600;line-height:30px;color:var(--ink);letter-spacing:-.5px}
.hotline{left:608px;top:24px;display:flex;gap:8px}
.hotline-label{font-size:10px;font-weight:700;color:var(--ink)}
.hotline-number{font-size:16px;color:var(--pink);font-weight:400}
.hotline-hours{font-size:8px;color:var(--grey);margin-top:2px}
.top-links{left:523px;top:74px;display:flex;gap:14px;font-size:9px;align-items:center;color:var(--ink)}
.top-links .on{color:var(--pink)}
.top-links .cart{color:var(--ink);margin-left:14px;display:flex;gap:4px;align-items:center}
.top-links .cart em{font-style:normal;color:var(--pink)}

/* nav */
.main-nav{position:absolute;left:0;top:105px;width:918px;height:43px;background:linear-gradient(#fafafa,#e6e6e6);border-bottom:4px solid var(--ink)}
.nav-list{position:absolute;left:61px;top:0;display:flex;height:39px;border-left:1px solid #d2d2d2}
.nav-list li{list-style:none;font-size:9.5px;font-weight:700;padding:0 8px;line-height:39px;border-right:1px solid #d2d2d2;color:#333}
.search{position:absolute;left:676px;top:10px;display:flex}
.search span{width:135px;height:22px;background:#fff;border:1px solid #ccc}
.search b{height:22px;background:var(--ink);color:#fff;font-size:9px;padding:0 6px;line-height:22px}

/* hero */
.hero{left:61px;top:171px;width:525px;height:263px;background:#1f1f1f;overflow:hidden;box-shadow:0 6px 8px rgba(0,0,0,.2)}
.hero-photo{position:absolute;left:0;top:0;width:300px;height:263px;background:linear-gradient(110deg,#f1e6df 0%,#d9b8a4 35%,#a8643c 60%,#6f3a1f 100%)}
.hero-tag{position:absolute;left:300px;top:21px;width:225px;height:34px;background:var(--pink);color:#fff;font-size:19px;font-weight:700;line-height:34px;padding-left:22px;clip-path:polygon(12px 0,100% 0,100% 100%,0 100%)}
.hero-title{position:absolute;left:321px;top:70px;color:#fff;font-size:27px;font-weight:600;line-height:28px}
.hero-sub{position:absolute;left:321px;top:130px;color:var(--pink);font-size:16px}
.hero-body{position:absolute;left:321px;top:155px;color:#999;font-size:9.5px;line-height:13px;width:180px}
.hero-buy{position:absolute;left:399px;top:198px;width:126px;height:36px;background:#fff;color:var(--pink);font-weight:700;font-size:16px;line-height:36px;padding-left:20px;clip-path:polygon(10px 0,100% 0,100% 100%,0 100%)}
.swatches{position:absolute;left:26px;top:196px;display:flex;gap:6px}
.swatches i{width:45px;height:45px;border-radius:50%;border:3px solid #fff;box-shadow:0 1px 3px rgba(0,0,0,.4)}
.arrow{position:absolute;top:117px}

.promo{left:606px;width:252px;height:121px;background:#1b1b1b;overflow:hidden}
.promo-photo{position:absolute;right:0;top:0;width:130px;height:121px;background:linear-gradient(90deg,#1b1b1b,#7a5a48 60%,#b88f74)}
.promo-text{position:absolute;left:17px;top:14px;color:#fff}
.promo-big{font-size:30px;font-weight:300;line-height:30px}
.promo-mid{font-size:21px;font-weight:600;line-height:24px}
.promo-pink{color:var(--pink);font-size:9.5px;font-weight:700}
.promo-buy{font-size:9.5px;font-weight:700;text-decoration:underline;margin-top:8px}

/* featured */
.section-title{left:61px;top:454px;width:797px;height:24px;border-bottom:1px solid var(--ink);border-left:6px solid var(--ink);padding-left:8px;color:var(--pink);font-weight:700;font-size:14px;line-height:18px}
.products{left:61px;top:500px;display:flex;gap:20px}
.card{width:184px;height:291px;border:1px solid var(--grey-light);position:relative}
.card-photo{position:absolute;left:22px;top:18px;width:140px;height:145px;background:linear-gradient(135deg,#f6efe7,#c7a27a)}
.card-name{position:absolute;left:18px;top:178px;width:150px;font-size:9.5px;line-height:13px;color:var(--pink)}
.card-price{position:absolute;left:18px;top:222px;font-size:15px}
.card-add{position:absolute;left:18px;top:250px;background:var(--ink);color:#fff;font-size:8.5px;padding:4px 7px}
.card-info{position:absolute;left:108px;top:248px}

/* shipping */
.ship{left:61px;top:811px;width:797px;height:27px;background:var(--ink);border-left:10px solid var(--pink);color:#aaa;font-size:13.5px;line-height:27px;padding-left:7px}
.ship b{color:#fff;letter-spacing:3px;font-size:16px}

.pay{left:61px;top:857px;display:flex;gap:6px}
.pay span{width:56px;height:37px;border:1px solid #ccc;border-radius:2px;background:linear-gradient(#fff,#e8e8e8);font-size:10px;font-weight:700;color:#2b3f8c;text-align:center;line-height:35px}
.follow{left:266px;top:866px;display:flex;align-items:center;gap:6px;color:var(--pink);font-size:13px;white-space:nowrap}
.follow .soc{display:flex;align-items:center;gap:3px;font-size:9px;color:var(--grey)}
.follow .soc i{width:12px;height:12px;border-radius:50%;background:#33c0e8}
.follow .soc i.blue{background:#3b5998}
.newsletter{left:470px;top:856px;font-size:10px;color:var(--pink)}
.newsletter div{display:flex;gap:8px;margin-top:5px}
.newsletter span{width:282px;height:22px;border:1px solid #ccc;font-size:8.5px;color:#aaa;line-height:20px;padding-left:8px}
.newsletter b{width:25px;height:22px;background:var(--ink);color:#fff;font-size:9px;text-align:center;line-height:22px}

.rule{left:61px;width:797px;height:1px;background:#ccc}
.about{left:61px;top:932px;width:797px;font-size:8.4px;line-height:12.5px;color:var(--grey)}

.footer-col{top:1024px;width:184px}
.footer-col h4{font-size:9.5px;color:var(--pink);font-weight:700;padding:0 0 9px 12px;border-bottom:1px solid #ccc;border-left:1px solid #ccc}
.footer-col ul{list-style:none;margin-top:20px}
.footer-col li{font-size:9px;font-weight:600;line-height:15.5px}
.footer-col p{font-size:9px;color:var(--grey);line-height:15.5px;margin-top:20px}
.copy{left:61px;top:1184px;font-size:8.5px;color:var(--grey)}
.copy em{font-style:normal;color:var(--pink)}
</style>
</head>
<body>
<div class="page">

<header class="site-header">
  <div class="abs brand"><span class="brand-mark"></span><div class="brand-name">Extensions<br>by Corvella</div></div>
  <div class="abs hotline">
    <svg width="30" height="30" viewBox="0 0 30 30"><circle cx="15" cy="15" r="13" fill="none" stroke="#aaa" stroke-width="2"/><path d="M10 9c1-1 2-1 3 0l1 3-2 1c1 2 2 3 4 4l1-2 3 1c1 1 1 2 0 3-3 2-11-6-10-10z" fill="#999"/></svg>
    <div>
      <div><span class="hotline-label">ASK OUR EXPERTS</span> <span class="hotline-number">1(800) 555-0142</span></div>
      <div class="hotline-hours">Hours: 9am 6pm PST M Th; 9am 3pm PST Fri</div>
    </div>
  </div>
  <nav class="abs top-links">
    <span class="on">Home</span><span>Contact</span><span>Sitemap</span>
    <span class="cart"><svg width="12" height="10" viewBox="0 0 12 10"><path d="M0 1h2l2 6h6l1-4H3" fill="none" stroke="#d6196f" stroke-width="1.4"/><circle cx="5" cy="9" r="1" fill="#d6196f"/><circle cx="9" cy="9" r="1" fill="#d6196f"/></svg>Cart <em>(empty)</em> ▾</span>
    <svg width="8" height="9" viewBox="0 0 8 9"><rect x="0" y="4" width="8" height="5" fill="#1b1b1b"/><path d="M2 4V2.5a2 2 0 0 1 4 0V4" fill="none" stroke="#1b1b1b" stroke-width="1.2"/></svg><span>En ▾</span><span>$ ▾</span>
  </nav>
</header>

<div class="main-nav">
  <ul class="nav-list">
    <li>CLIP IN HAIR EXTENSION</li><li>WEAVE &amp; WEFT</li><li>PRE BONDED &amp; FUSION</li><li>MICRO LOOP</li><li>CLIP IN HIGHLIGHT</li>
  </ul>
  <div class="search"><span></span><b>SEARCH:</b></div>
</div>

<section class="abs hero">
  <div class="hero-photo" role="img" aria-label="Woman with long auburn hair extensions"></div>
  <div class="hero-tag">SPECIAL OFFER</div>
  <div class="hero-title">CLIP IN HAIR<br>EXTENSION</div>
  <div class="hero-sub">Get up to 25% off</div>
  <div class="hero-body">Lorem ipsum dolor sit amet conse ctetur adipiscing elit, sed do eiusmod</div>
  <div class="hero-buy">BUY NOW!</div>
  <div class="swatches"><i style="background:#1c1c1c"></i><i style="background:#4a2a1a"></i><i style="background:#7b4524"></i><i style="background:#8f5a34"></i><i style="background:#a9764a"></i><i style="background:#d4b486"></i></div>
  <svg class="arrow" style="left:6px" width="12" height="22" viewBox="0 0 12 22"><path d="M10 2 2 11l8 9" fill="none" stroke="#333" stroke-width="2"/></svg>
  <svg class="arrow" style="left:508px" width="12" height="22" viewBox="0 0 12 22"><path d="M2 2l8 9-8 9" fill="none" stroke="#fff" stroke-width="2"/></svg>
</section>

<aside class="abs promo" style="top:171px">
  <div class="promo-photo" role="img" aria-label="Woman with flowing dark hair"></div>
  <div class="promo-text"><div class="promo-big">HAIR</div><div class="promo-mid">EXTENSIONS</div><div class="promo-pink">EXTEND YOUR BEAUTY</div><div class="promo-buy">BUY NOW!</div></div>
</aside>
<aside class="abs promo" style="top:313px">
  <div class="promo-photo" role="img" aria-label="Woman wearing a curly blonde wig"></div>
  <div class="promo-text"><div class="promo-big">HIGH</div><div class="promo-mid" style="color:var(--pink);font-size:17px">QUALITY WIGS</div><div style="font-size:9px;color:#777;line-height:11px">BECOME ANOTHER YOU<br>IN MINUTES</div><div class="promo-buy" style="margin-top:2px">BUY NOW!</div></div>
</aside>

<h2 class="abs section-title">FEATURED PRODUCTS</h2>

<section class="abs products">
  <article class="card"><div class="card-photo" role="img" aria-label="Braided chignon bun in golden wheat"></div><div class="card-name">Lunara Hairdo Braided Chignon Clip In Bun Hair Golden Wheat</div><div class="card-price">$528.96</div><div class="card-add">ADD TO CART</div><svg class="card-info" width="20" height="20" viewBox="0 0 20 20"><circle cx="10" cy="10" r="10" fill="#ccc"/><rect x="9" y="8" width="2" height="7" fill="#fff"/><circle cx="10" cy="5.5" r="1.3" fill="#fff"/></svg></article>
  <article class="card"><div class="card-photo" style="background:linear-gradient(135deg,#f7f2ef,#3a2520)" role="img" aria-label="Dark brown wrap-around ponytail"></div><div class="card-name">Starline Clip-In Hair Extensions 18 Wrap Around Ponytail</div><div class="card-price">$122.51</div><div class="card-add">ADD TO CART</div><svg class="card-info" width="20" height="20" viewBox="0 0 20 20"><circle cx="10" cy="10" r="10" fill="#ccc"/><rect x="9" y="8" width="2" height="7" fill="#fff"/><circle cx="10" cy="5.5" r="1.3" fill="#fff"/></svg></article>
  <article class="card"><div class="card-photo" style="background:linear-gradient(135deg,#e9c98e,#f2dcc8 55%,#b56aa8)" role="img" aria-label="Model with highlighted clip-in extensions"></div><div class="card-name">Premium 6 Piece Highlighted Clip In Human Hair Extensions</div><div class="card-price">$394.64</div><div class="card-add">ADD TO CART</div><svg class="card-info" width="20" height="20" viewBox="0 0 20 20"><circle cx="10" cy="10" r="10" fill="#ccc"/><rect x="9" y="8" width="2" height="7" fill="#fff"/><circle cx="10" cy="5.5" r="1.3" fill="#fff"/></svg></article>
  <article class="card"><div class="card-photo" style="background:linear-gradient(135deg,#fbf3ee,#c08566)" role="img" aria-label="Hair bow knot on a brown comb clip"></div><div class="card-name">Bow Hair Extension Bowknot Brown Comb Clip Fashion Hairpiece Party</div><div class="card-price">$394.64</div><div class="card-add">ADD TO CART</div><svg class="card-info" width="20" height="20" viewBox="0 0 20 20"><circle cx="10" cy="10" r="10" fill="#ccc"/><rect x="9" y="8" width="2" height="7" fill="#fff"/><circle cx="10" cy="5.5" r="1.3" fill="#fff"/></svg></article>
</section>

<div class="abs ship"><b>FREE SHIPPING</b> ON ORDERS OVER $ 99. THIS OFFER IS VALID ON ALL OUR STORE ITEMS.</div>

<div class="abs pay"><span>Veyra</span><span>PayLoom</span><span style="font-size:8.5px">MeridCard</span></div>
<div class="abs follow">FOLLOW US: <span class="soc"><i></i>Chirpline</span><span class="soc"><i class="blue"></i>Facenest</span></div>
<div class="abs newsletter">NEWSLETTER<div><span>Your email address</span><b>OK</b></div></div>

<div class="abs rule" style="top:914px"></div>
<p class="abs about">Lorem ipsum dolor sit amet conse ctetur adipiscing elit, sed do eiusmod tempor incididunt ut labore et dolore magna aliqua. Ut enim ad minim veniam, quis nostrud exercitation ullamco laboris nisi ut aliquip ex ea commodo consequat. Duis aute irure dolor in reprehenderit in voluptate velit esse cillum dolore eu fugiat nulla pariatur. Lorem ipsum dolor sit amet conse ctetur adipiscing elit, sed do eiusmod tempor incididunt ut labore et dolore magna aliqua. Ut enim ad minim veniam, quis nostrud exercitation ullamco laboris nisi ut aliquip ex ea commodo consequat. Duis aute irure dolor in reprehenderit in voluptate velit esse cillum dolore eu fugiat nulla pariatur. Excepteur sint occaecat cupidatat non proident, sunt in culpa qui officia deserunt mollit anim id est laborum.</p>
<div class="abs rule" style="top:1001px"></div>

<footer>
  <div class="abs footer-col" style="left:61px"><h4>CATEGORIES</h4><ul><li>Clip in hair extension</li><li>Weave &amp; Weft</li><li>Pre bonded &amp; fusion</li><li>Micro loop</li><li>Clip in highlight</li></ul></div>
  <div class="abs footer-col" style="left:265px"><h4>INFORMATION</h4><ul><li>Specials</li><li>New products</li><li>Best sellers</li><li>Our stores</li><li>Contact us</li><li>Sitemap</li></ul></div>
  <div class="abs footer-col" style="left:470px"><h4>MY ACCOUNT</h4><ul><li>My orders</li><li>My addresses</li><li>My personal info</li><li>My favorite products.</li></ul></div>
  <div class="abs footer-col" style="left:674px"><h4>CONTACT US</h4><p>Chicago · Illinois · USA<br>Tel +1 312 555 0187</p></div>
  <div class="abs rule" style="top:1177px"></div>
  <div class="abs copy">© 2014 Powered by <em>Brightloom Studio</em>™</div>
</footer>

</div>
</body>
</html>
```